Interior Stylist business card design needed

I need a business card for my new company in Sydney called "Lu Brannigan Designs". The business offers an interior styling and colour consultancy. My clients are generally not very design savvy (hence why they use me) and can range from being quite conservative to really wanting something "out there". They can be looking for a budget makeover or something more expensive / substantial. I'd like my business card design to be stylish (but not overly formal). I certainly don't want it to be conservative. I'd like it to stand out a bit! I don't really have any aversion to particular colours and I don't have a logo as such - my business name is really all I have.

Target Market(s)

As above - home owners, ranging from conservative to modern

Industry/Entity Type

Conservative

Contact Information for Business Card

Lu Brannigan Designs
Colour consultancy and interior styling
ph: 0417 368 205
email: lubrannigan@zephmail.net.au

Requirements
Should not have
• Old fashioned writing or motifs. No Times Roman font!!

```html
<!DOCTYPE html>
<html lang="en">
<head>
<meta charset="utf-8">
<title>Lu Brannigan Designs – Business Cards</title>
<link rel="stylesheet" href="https://fonts.googleapis.com/css2?family=Cinzel:wght@400;600&family=Open+Sans:wght@400&display=swap">
<style>
  :root {
    --teal: #2f6b68;
    --teal-soft: #4f8784;
    --paper: #ffffff;
    --backdrop: #ecebe8;
    --shadow: rgba(0, 0, 0, 0.18);
  }
  * { margin: 0; padding: 0; box-sizing: border-box; }
  html, body {
    width: 1200px;
    height: 787px;
    overflow: hidden;
    background: var(--backdrop);
  }
  .canvas {
    position: relative;
    width: 1200px;
    height: 787px;
  }
  .card {
    position: absolute;
    top: 239px;
    width: 540px;
    height: 309px;
    background: var(--paper);
    box-shadow: 0 6px 18px var(--shadow);
    overflow: hidden;
  }
  .card--front { left: 40px; }
  .card--back { left: 620px; }

  /* Front card */
  .frame {
    position: absolute;
    inset: 14px;
    border: 16px solid var(--teal);
    border-radius: 6px;
  }
  .monogram {
    position: absolute;
    left: 206px;
    top: 78px;
    width: 118px;
    height: 66px;
    background: var(--teal);
    opacity: 0.85;
    border-radius: 4px;
  }
  .front-name {
    position: absolute;
    left: 0;
    right: 0;
    top: 156px;
    text-align: center;
    font-family: "Cinzel", serif;
    font-weight: 600;
    font-size: 24px;
    letter-spacing: 1px;
    color: var(--teal);
  }
  .front-web {
    position: absolute;
    left: 0;
    right: 0;
    top: 206px;
    text-align: center;
    font-family: "Open Sans", sans-serif;
    font-size: 12px;
    color: var(--teal);
  }

  /* Back card */
  .band {
    position: absolute;
    inset: 0;
    width: 540px;
    height: 309px;
  }
  .brand {
    position: absolute;
    left: 0;
    right: 0;
    top: 62px;
    text-align: center;
    color: var(--teal);
    font-family: "Cinzel", serif;
  }
  .brand__name {
    font-weight: 600;
    font-size: 26px;
    letter-spacing: 1px;
  }
  .brand__tag {
    margin-top: 2px;
    font-size: 13px;
    letter-spacing: 9px;
  }
  .contacts {
    position: absolute;
    left: 26px;
    top: 226px;
    list-style: none;
    font-family: "Open Sans", sans-serif;
    font-size: 11px;
    color: var(--paper);
  }
  .contacts li {
    display: flex;
    align-items: center;
    gap: 8px;
    height: 17px;
  }
  .contacts svg { width: 11px; height: 11px; flex: none; }
  .contacts .dot {
    width: 10px;
    height: 10px;
    background: var(--paper);
    border-radius: 2px;
    flex: none;
  }
  .back-monogram {
    position: absolute;
    left: 400px;
    top: 238px;
    width: 92px;
    height: 54px;
    background: var(--teal-soft);
    border-radius: 4px;
  }
</style>
</head>
<body>
<main class="canvas">

  <section class="card card--front" aria-label="Business card front">
    <div class="frame"></div>
    <div class="monogram" role="img" aria-label="Handwritten LB monogram"></div>
    <p class="front-name">LU BRANNIGAN</p>
    <p class="front-web">www.lubrannigan.com</p>
  </section>

  <section class="card card--back" aria-label="Business card back">
    <svg class="band" viewBox="0 0 540 309" aria-hidden="true">
      <polygon points="0,200 540,262 540,309 0,309" fill="var(--teal)"/>
      <line x1="210" y1="218" x2="540" y2="255" stroke="var(--teal)" stroke-width="1.5"/>
      <line x1="330" y1="228" x2="540" y2="250" stroke="var(--teal)" stroke-width="1"/>
    </svg>
    <div class="brand">
      <p class="brand__name">LU BRANNIGAN</p>
      <p class="brand__tag">DESIGNS</p>
    </div>
    <ul class="contacts">
      <li>
        <svg viewBox="0 0 12 12"><path d="M3 1l2 2.5-1.2 1.2a6 6 0 0 0 3.5 3.5L8.5 7 11 9l-1.5 2A9 9 0 0 1 1 2.5z" fill="var(--paper)"/></svg>
        0417 368 205
      </li>
      <li>
        <svg viewBox="0 0 12 12"><rect x="1" y="2.5" width="10" height="7" fill="none" stroke="var(--paper)" stroke-width="1.2"/><path d="M1 2.5l5 4 5-4" fill="none" stroke="var(--paper)" stroke-width="1.2"/></svg>
        lubrannigan@zephmail.net.au
      </li>
      <li>
        <span class="dot"></span>
        www.linkpage.com/lubrannigan
      </li>
    </ul>
    <div class="back-monogram" role="img" aria-label="Handwritten LB monogram"></div>
  </section>

</main>
</body>
</html>
```